Harbor of Mercy - Team of Rabbis and Doctors Helping Families Dealing with Illness

The Harbor of Mercy is an organization that accompanies families dealing with severe illnesses of a family member. A team of rabbis and doctors provide support and real-time responses to these families.
The site theme is medicine and law, but the target market is religious Jewish families in crisis. Thus, the site design needs to combine:
- professional, conservative, serious
- spiritual
- warm hug

Target Market(s)

religious families suffering a health crisis

Industry/Entity Type

Non-profit organization

Number of Pages Required

1 page

Font styles to use
Sans Serif

Requirements
Must have
• Final design in PSD format. List of fonts used, colors used and link/button colors used in the design.

```html
<!DOCTYPE html>
<html lang="en">
<head>
<meta charset="utf-8">
<title>Harbor of Mercy</title>
<link href="https://fonts.googleapis.com/css2?family=Montserrat:wght@400;500;600;700;800&display=swap" rel="stylesheet">
<style>
:root{
  --blue:#03497f;
  --blue-dark:#023a68;
  --gold:#f7b92e;
  --gold-btn:#fbbf2c;
  --hero-gold:#d5b419;
  --text:#333;
  --muted:#555;
  --white:#fff;
  --line:#e6e6e6;
}
*{box-sizing:border-box;margin:0;padding:0}
html,body{width:1200px;height:4213px;overflow:hidden}
body{position:relative;font-family:"Montserrat",sans-serif;color:var(--text);background:var(--white)}
.abs{position:absolute}
a{color:inherit;text-decoration:none}

/* top bar */
.topbar{left:0;top:0;width:1200px;height:57px;background:var(--blue)}
.search{left:141px;top:13px;width:173px;height:33px;border:2px solid var(--gold);border-radius:17px;background:var(--blue-dark);color:#9fb4c8;font-size:11px;padding:8px 0 0 18px}
.search-btn{right:-2px;top:-2px;width:33px;height:33px;border-radius:0 17px 17px 0;background:var(--gold);display:flex;align-items:center;justify-content:center}
.round{width:28px;height:28px;border-radius:50%;background:var(--gold);display:flex;align-items:center;justify-content:center}
.top-text{color:var(--white);font-size:12px;font-weight:500}
.dedication{height:36px;background:var(--gold);color:var(--blue);font-weight:700;font-size:12px;display:flex;align-items:center;justify-content:center;border-radius:3px}

/* nav */
.nav{left:0;top:57px;width:1200px;height:79px;border-bottom:1px solid var(--line)}
.nav a{position:absolute;top:32px;font-size:12px;font-weight:600;color:#222}
.brand{font-weight:800;color:var(--gold);font-size:20px;display:flex;align-items:center;gap:8px}
.brand .sq{width:14px;height:14px;background:var(--blue)}

/* hero */
.hero{left:0;top:136px;width:1200px;height:521px;background:linear-gradient(90deg,var(--hero-gold) 0%,#d2b21c 42%,#9a7d1f 62%,#3d2a12 100%)}
.hero ul{position:absolute;left:141px;top:348px;list-style:none}
.hero li{color:#1f1f1f;font-size:16px;font-weight:500;line-height:36px;padding-left:22px;position:relative}
.hero li::before{content:"";position:absolute;left:0;top:15px;width:7px;height:7px;border-radius:50%;background:#222}
.hero-arrow{width:36px;height:36px;border-radius:50%;display:flex;align-items:center;justify-content:center}

/* about */
.photo{border-radius:8px}
.h2{font-size:41px;font-weight:800;color:var(--gold)}
.about-text{left:608px;top:828px;width:450px;font-size:11.5px;line-height:21.6px;color:#333}
.about-text p{margin-bottom:5px}
.btn-blue{background:var(--blue);color:var(--white);font-size:12.5px;font-weight:600;display:flex;align-items:center;justify-content:center;border-radius:3px}
.btn-gold{background:var(--gold-btn);color:var(--blue);font-size:12.5px;font-weight:600;display:flex;align-items:center;justify-content:center;border-radius:3px}

/* moral */
.moral{left:0;top:1287px;width:1200px;height:551px;background:var(--blue)}
.moral-intro{left:144px;top:1444px;width:330px;color:var(--white);font-size:11.5px;line-height:21.5px}
.checks{left:144px;top:1521px;width:340px;list-style:none;color:var(--white);font-size:11.5px;line-height:20px}
.checks li{position:relative;padding-left:20px;margin-bottom:8px}
.checks svg{position:absolute;left:0;top:3px}
.dot{width:7px;height:7px;border-radius:50%;background:#b9c7d6}

/* services */
.card{top:1929px;height:270px;background:var(--white);box-shadow:0 4px 14px rgba(0,0,0,.09);text-align:center}
.card svg{margin-top:38px}
.card h3{font-size:20px;font-weight:700;color:var(--blue);margin-top:14px}
.card p{font-size:11.5px;line-height:20.5px;color:#444;margin:10px 18px 0}
.card a{display:inline-block;margin-top:7px;font-size:11px;font-weight:700;color:#222;text-decoration:underline}

/* testimonials */
.testi{left:0;top:2294px;width:1200px;height:559px;background:var(--blue)}
.center-h{left:0;width:1200px;text-align:center}
.quote-box{left:181px;top:2493px;width:826px;height:254px;background:var(--white);border-radius:3px;text-align:center}
.quote-box p{width:680px;margin:60px auto 0;font-size:11.5px;line-height:28px;color:#444}
.quote-box h4{margin-top:14px;font-size:20px;font-weight:700;color:var(--gold)}

/* news */
.news{width:437px;height:139px;background:var(--white);border:1px solid var(--line)}
.news .thumb{position:absolute;left:6px;top:6px;width:200px;height:126px}
.news .date{position:absolute;left:225px;top:24px;font-size:12.5px;color:#333;display:flex;align-items:center;gap:6px}
.news h5{position:absolute;left:225px;top:50px;width:200px;font-size:14.5px;font-weight:500;line-height:20px;color:#222}

/* cta */
.cta{left:0;top:3409px;width:1200px;height:446px;background:linear-gradient(180deg,#1d4f80 0%,#2a5d8c 55%,#1c4a79 100%)}
.cta h2{position:absolute;left:0;top:156px;width:1200px;text-align:center;color:var(--gold);font-size:25px;font-weight:700;line-height:43px}

/* footer */
.footer h4{font-size:18px;font-weight:800;color:#111}
.flinks{list-style:none;font-size:11.5px;font-weight:500;color:#222;line-height:22.5px}
.flinks li::before{content:"»";color:var(--gold);margin-right:8px;font-size:11px}
.fline{font-size:11.5px;font-weight:500;line-height:19px;color:#222}
.flabel{font-size:11.5px;font-weight:700;color:#111}
.copy{left:0;top:4169px;width:1200px;height:44px;background:var(--gold-btn);text-align:center;font-size:11.5px;font-weight:600;color:var(--blue);line-height:44px}
</style>
</head>
<body>

<!-- top bar -->
<div class="abs topbar"></div>
<div class="abs search">Search...
  <div class="abs search-btn"><svg width="14" height="14" viewBox="0 0 14 14"><circle cx="6" cy="6" r="4.3" fill="none" stroke="#03497f" stroke-width="1.8"/><path d="M9.2 9.2 12.5 12.5" stroke="#03497f" stroke-width="1.8"/></svg></div>
</div>
<div class="abs round" style="left:326px;top:15px"></div>
<div class="abs round" style="left:368px;top:15px"><svg width="14" height="11" viewBox="0 0 14 11"><rect x=".7" y=".7" width="12.6" height="9.6" fill="none" stroke="#03497f" stroke-width="1.3"/><path d="M1 1l6 5 6-5" fill="none" stroke="#03497f" stroke-width="1.3"/></svg></div>
<div class="abs top-text" style="left:405px;top:21px">info@harborofmercy.org</div>
<div class="abs round" style="left:578px;top:15px"><svg width="14" height="14" viewBox="0 0 14 14"><path d="M3 1.5 5.2 1l1.2 3-1.5 1.2a8 8 0 0 0 3.9 3.9L10 7.6l3 1.2-.5 2.2C7 11.5 2.5 7 3 1.5z" fill="#03497f"/></svg></div>
<div class="abs top-text" style="left:613px;top:21px"><b>Hot Line :</b> 123-456-7890</div>
<div class="abs dedication" style="left:772px;top:10px;width:137px">DEDICATION 2</div>
<div class="abs dedication" style="left:919px;top:10px;width:140px">DEDICATION 1</div>

<!-- nav -->
<nav class="abs nav">
  <a style="left:141px">Home</a>
  <a style="left:204px">About Us</a>
  <a style="left:289px">Courses</a>
  <a style="left:366px">Conferences</a>
  <a style="left:471px">Lectures</a>
  <a style="left:551px">News</a>
  <a style="left:613px">Contact Us</a>
</nav>
<div class="abs brand" style="left:880px;top:84px"><span class="sq"></span>Harbor of Mercy</div>

<!-- hero -->
<section class="abs hero">
  <div role="img" aria-label="Hands lighting candles on a menorah beside a handwritten note" class="abs" style="left:540px;top:0;width:660px;height:521px;background:radial-gradient(ellipse at 60% 40%,rgba(240,200,110,.35),rgba(0,0,0,0) 60%)"></div>
  <ul>
    <li>Should morphine be given to the patient?</li>
    <li>Should the patient be resuscitated?</li>
    <li>Should cancer patients continue treatment?</li>
  </ul>
  <div class="abs hero-arrow" style="left:77px;top:243px;border:2px solid #333"><svg width="10" height="14" viewBox="0 0 10 14"><path d="M7 2 2 7l5 5" fill="none" stroke="#222" stroke-width="2"/></svg></div>
  <div class="abs hero-arrow" style="left:1086px;top:243px;background:var(--gold)"><svg width="10" height="14" viewBox="0 0 10 14"><path d="M3 2l5 5-5 5" fill="none" stroke="#fff" stroke-width="2"/></svg></div>
</section>

<!-- about -->
<div role="img" aria-label="Father and son reading a prayer book at a festive table with candles" class="abs photo" style="left:141px;top:744px;width:426px;height:450px;background:linear-gradient(135deg,#5a3a22,#a7774a 45%,#3b2515)"></div>
<div class="abs" style="left:321px;top:947px;width:54px;height:54px;border:3px solid #fff;border-radius:50%;display:flex;align-items:center;justify-content:center"><svg width="18" height="22" viewBox="0 0 18 22"><path d="M3 2l13 9-13 9z" fill="#fff"/></svg></div>
<h2 class="abs h2" style="left:608px;top:770px">About Us</h2>
<div class="abs about-text">
  <p>Lorem ipsum dolor sit amet, consectetur adipiscing elit, sed do eiusmod ese tempor incididunt ut labore et dolore magna aliqua. Ut enim ad minim lorem veniam, quis nostrud exercitation ullamco laboris nisi ut aliquip ex ea ipsum commodo consequat Lorem ipsum dolor sit amet, consectetur adipiscinges elit, sed do eiusmod tempor incididunt ut labore et dolore magna aliqua. Ut enim ad minim veniam, quis nostrud exercitation ullamco laboris nisi ut lore aliquip ex ea commodo consequat</p>
  <p>Lorem ipsum dolor sit amet, consectetur adipiscing elit, sed do eiusmod ese tempor incididunt ut labore et dolore magna aliqua. Ut enim ad minim lorem veniam, quis nostrud exercitation ullamco laboris nisi ut</p>
  <p>Lorem ipsum dolor sit amet, consectetur adipiscing elit, sed do eiusmod ese tempor incididunt ut labore et dolore magna aliqua.</p>
</div>
<a class="abs btn-blue" style="left:608px;top:1118px;width:147px;height:38px">Contact Us</a>

<!-- moral issues -->
<section class="abs moral"></section>
<h2 class="abs h2" style="left:144px;top:1388px">Moral Issues</h2>
<p class="abs moral-intro">Lorem ipsum dolor sit amet, consectetur adipiscing elit, sed do eiusmod ese tempor incididunt ut labore et dolore magna aliqua. Ut enim</p>
<ul class="abs checks" style="top:1524px">
  <li><svg width="13" height="13" viewBox="0 0 13 13"><circle cx="6.5" cy="6.5" r="5.7" fill="none" stroke="#f7b92e" stroke-width="1.2"/><path d="M3.8 6.7l1.8 1.8 3.6-3.7" fill="none" stroke="#f7b92e" stroke-width="1.2"/></svg>consectetur adipiscing elit sed do eiusmod ese tempor iet dolore magna aliqua</li>
  <li><svg width="13" height="13" viewBox="0 0 13 13"><circle cx="6.5" cy="6.5" r="5.7" fill="none" stroke="#f7b92e" stroke-width="1.2"/><path d="M3.8 6.7l1.8 1.8 3.6-3.7" fill="none" stroke="#f7b92e" stroke-width="1.2"/></svg>Lorem ipsum dolor sit amet consectetur adipiscing</li>
  <li><svg width="13" height="13" viewBox="0 0 13 13"><circle cx="6.5" cy="6.5" r="5.7" fill="none" stroke="#f7b92e" stroke-width="1.2"/><path d="M3.8 6.7l1.8 1.8 3.6-3.7" fill="none" stroke="#f7b92e" stroke-width="1.2"/></svg>consectetur adipiscing elit sed do eiusmod ese tempor iet dolore magna aliqua</li>
  <li><svg width="13" height="13" viewBox="0 0 13 13"><circle cx="6.5" cy="6.5" r="5.7" fill="none" stroke="#f7b92e" stroke-width="1.2"/><path d="M3.8 6.7l1.8 1.8 3.6-3.7" fill="none" stroke="#f7b92e" stroke-width="1.2"/></svg>Lorem ipsum dolor sit amet consectetur adipiscing</li>
</ul>
<a class="abs btn-gold" style="left:142px;top:1689px;width:146px;height:38px">Ask The Rabbi</a>
<div role="img" aria-label="Older man and young woman studying a book together" class="abs photo" style="left:556px;top:1373px;width:314px;height:378px;background:linear-gradient(160deg,#4a4642,#8a7a66 50%,#2e2a26)"></div>
<div role="img" aria-label="Hand lighting candles on a menorah in the dark" class="abs photo" style="left:886px;top:1373px;width:314px;height:378px;border-radius:8px 0 0 8px;background:radial-gradient(ellipse at 75% 30%,#8a5a22,#2a1a10 55%,#120c08)"></div>
<div class="abs dot" style="left:863px;top:1771px"></div>
<div class="abs dot" style="left:879px;top:1771px;background:var(--gold)"></div>
<div class="abs dot" style="left:895px;top:1771px"></div>
<div class="abs dot" style="left:911px;top:1771px"></div>

<!-- services -->
<div class="abs card" style="left:141px;width:219px">
  <svg width="52" height="56" viewBox="0 0 52 56"><path d="M14 10l12-6 12 6-12 6z" fill="none" stroke="#f7b92e" stroke-width="2"/><path d="M8 22h16v28H8zM28 22h16v28H28z" fill="none" stroke="#03497f" stroke-width="2"/><path d="M12 30h8M12 36h8M32 30h8M32 36h8" stroke="#03497f" stroke-width="1.6"/></svg>
  <h3>Courses</h3><p>Lorem ipsum dolor sit amet, consectetur adipiscing elit sed do eiusmod tempor</p><a>Know More</a>
</div>
<div class="abs card" style="left:373px;width:221px">
  <svg width="56" height="56" viewBox="0 0 56 56"><rect x="4" y="4" width="16" height="12" fill="none" stroke="#f7b92e" stroke-width="2"/><circle cx="34" cy="12" r="5" fill="none" stroke="#03497f" stroke-width="2"/><path d="M24 30h20v8H24zM26 22h16v8" fill="none" stroke="#03497f" stroke-width="2"/><circle cx="12" cy="40" r="4" fill="none" stroke="#03497f" stroke-width="2"/><circle cx="28" cy="44" r="4" fill="none" stroke="#03497f" stroke-width="2"/><circle cx="44" cy="44" r="4" fill="none" stroke="#03497f" stroke-width="2"/><path d="M5 52a7 7 0 0 1 14 0M21 55a7 7 0 0 1 14 0M37 55a7 7 0 0 1 14 0" fill="none" stroke="#03497f" stroke-width="2"/></svg>
  <h3>Conferences</h3><p>Lorem ipsum dolor sit amet, consectetur adipiscing elit sed do eiusmod tempor</p><a>Know More</a>
</div>
<div class="abs card" style="left:607px;width:219px">
  <svg width="56" height="56" viewBox="0 0 56 56"><rect x="22" y="4" width="30" height="22" fill="none" stroke="#f7b92e" stroke-width="2"/><path d="M28 12h18M28 18h12" stroke="#f7b92e" stroke-width="1.6"/><circle cx="12" cy="12" r="5" fill="none" stroke="#03497f" stroke-width="2"/><path d="M4 34c0-8 4-12 8-12s6 2 10-2" fill="none" stroke="#03497f" stroke-width="2"/><circle cx="32" cy="40" r="4" fill="none" stroke="#03497f" stroke-width="2"/><circle cx="46" cy="40" r="4" fill="none" stroke="#03497f" stroke-width="2"/><path d="M25 52a7 7 0 0 1 14 0M39 52a7 7 0 0 1 14 0" fill="none" stroke="#03497f" stroke-width="2"/></svg>
  <h3>Lectures</h3><p>Lorem ipsum dolor sit amet, consectetur adipiscing elit sed do eiusmod tempor</p><a>Know More</a>
</div>
<div class="abs card" style="left:839px;width:220px">
  <svg width="56" height="56" viewBox="0 0 56 56"><circle cx="30" cy="28" r="17" fill="none" stroke="#03497f" stroke-width="2"/><text x="30" y="33" text-anchor="middle" font-family="Montserrat,sans-serif" font-size="13" font-weight="700" fill="#f7b92e">24</text><path d="M6 20l6-6 5 6-4 4a14 14 0 0 0 6 10l-3 4z" fill="none" stroke="#03497f" stroke-width="2"/></svg>
  <h3>Hotline 24/7</h3><p>Lorem ipsum dolor sit amet, consectetur adipiscing elit sed do eiusmod tempor</p><a>Know More</a>
</div>

<!-- testimonials -->
<section class="abs testi"></section>
<h2 class="abs h2 center-h" style="top:2367px">Testimonials</h2>
<div class="abs quote-box">
  <p>Lorem ipsum dolor sit amet, consectetuer adipiscing elit, sed diam nonummy nibh euismod tincidunt ut laoreet dolore magna aliquam erat volutpat. Ut wisi enim ad minim veniam, quis nostrud exerci tation ullamcorper suscipit lobortis nisl ut aliquip ex ea commodo consequat. Duis autem vel eum iriure dolor in hendrerit in vulputate velit esse molestie consequat, vel illum dolore eu feugiat nulla facilisis.</p>
  <h4>Joseph Doe</h4>
</div>
<svg class="abs" style="left:552px;top:2455px" width="86" height="66" viewBox="0 0 86 66"><path d="M30 2C12 10 2 26 2 44a18 18 0 1 0 20-18c2-8 6-14 14-20z" fill="#f7c95e"/><path d="M76 2C58 10 48 26 48 44a18 18 0 1 0 20-18c2-8 6-14 14-20z" fill="#f7c95e"/></svg>
<svg class="abs" style="left:153px;top:2609px" width="70" height="20" viewBox="0 0 70 20"><path d="M68 10H4M12 3 3 10l9 7" fill="none" stroke="#9aa7b5" stroke-width="2.5"/></svg>
<svg class="abs" style="left:966px;top:2609px" width="70" height="20" viewBox="0 0 70 20"><path d="M2 10h64M58 3l9 7-9 7" fill="none" stroke="#f7b92e" stroke-width="2.5"/></svg>

<!-- news -->
<h2 class="abs h2 center-h" style="top:2930px">Latest News</h2>
<div class="abs news" style="left:141px;top:3015px">
  <div class="thumb" role="img" aria-label="Decorated wall with blue stars and a person reaching up" style="background:linear-gradient(135deg,#c9b89a,#7f8fa5 55%,#2a2a2a)"></div>
  <div class="date"><svg width="12" height="12" viewBox="0 0 12 12"><rect x="1" y="2" width="10" height="9" fill="none" stroke="#333" stroke-width="1.3"/><path d="M1 5h10M4 1v2M8 1v2" stroke="#333" stroke-width="1.3"/></svg>SEPT 10, 2023</div>
  <h5>Lorem Ipsum Dolor Sit Consectetuer Adipiscing</h5>
</div>
<div class="abs news" style="left:620px;top:3015px">
  <div class="thumb" role="img" aria-label="Group of people talking in a bright office" style="background:linear-gradient(135deg,#e3ddd3,#9a8a78 55%,#4d4036)"></div>
  <div class="date"><svg width="12" height="12" viewBox="0 0 12 12"><rect x="1" y="2" width="10" height="9" fill="none" stroke="#333" stroke-width="1.3"/><path d="M1 5h10M4 1v2M8 1v2" stroke="#333" stroke-width="1.3"/></svg>Nov 3, 2023</div>
  <h5>Lorem Ipsum Dolor Sit Consectetuer Adipiscing</h5>
</div>
<div class="abs news" style="left:141px;top:3178px">
  <div class="thumb" role="img" aria-label="Hand lighting a candle by a window" style="background:linear-gradient(135deg,#3a2a1a,#b78a52 50%,#e9d8b8)"></div>
  <div class="date"><svg width="12" height="12" viewBox="0 0 12 12"><rect x="1" y="2" width="10" height="9" fill="none" stroke="#333" stroke-width="1.3"/><path d="M1 5h10M4 1v2M8 1v2" stroke="#333" stroke-width="1.3"/></svg>OCT 27, 2023</div>
  <h5>Lorem Ipsum Dolor Sit Consectetuer Adipiscing</h5>
</div>
<div class="abs news" style="left:620px;top:3178px">
  <div class="thumb" role="img" aria-label="Study group reading together around a table" style="background:linear-gradient(135deg,#2e2418,#8a6a42 50%,#3a2e22)"></div>
  <div class="date"><svg width="12" height="12" viewBox="0 0 12 12"><rect x="1" y="2" width="10" height="9" fill="none" stroke="#333" stroke-width="1.3"/><path d="M1 5h10M4 1v2M8 1v2" stroke="#333" stroke-width="1.3"/></svg>DEC 11, 2023</div>
  <h5>Lorem Ipsum Dolor Sit Consectetuer Adipiscing</h5>
</div>

<!-- call to action -->
<section class="abs cta" role="img" aria-label="Blue-tinted view of an old city skyline">
  <h2>Lorem Ipsum Dolor Sit Amet Consectetur Adipiscing Elit Sed Do<br>Eiusmod Tempor Incididunt Ut Labore Et Dolore Magna</h2>
</section>
<a class="abs btn-gold" style="left:526px;top:3661px;width:146px;height:37px">Ask The Rabbi</a>

<!-- footer -->
<footer class="footer">
  <h4 class="abs" style="left:142px;top:3920px">Quick Links</h4>
  <ul class="abs flinks" style="left:145px;top:3948px">
    <li>Home</li><li>About Us</li><li>Courses</li><li>Conferences</li><li>Lectures</li><li>News</li><li>Contact Us</li>
  </ul>
  <h4 class="abs" style="left:317px;top:3920px">Contact Details</h4>
  <svg class="abs" style="left:317px;top:3954px" width="12" height="15" viewBox="0 0 12 15"><path d="M6 14S1 8.5 1 5.5a5 5 0 0 1 10 0C11 8.5 6 14 6 14z" fill="#03497f"/><circle cx="6" cy="5.5" r="1.8" fill="#fff"/></svg>
  <div class="abs fline" style="left:337px;top:3951px;width:180px">52 Cedar Lane, Brookfield, AR 12345</div>
  <svg class="abs" style="left:317px;top:4002px" width="13" height="13" viewBox="0 0 14 14"><path d="M3 1.5 5.2 1l1.2 3-1.5 1.2a8 8 0 0 0 3.9 3.9L10 7.6l3 1.2-.5 2.2C7 11.5 2.5 7 3 1.5z" fill="#03497f"/></svg>
  <div class="abs flabel" style="left:338px;top:4004px">PHONE</div>
  <div class="abs fline" style="left:338px;top:4022px">+1 123 456 7890</div>
  <svg class="abs" style="left:317px;top:4055px" width="14" height="11" viewBox="0 0 14 11"><rect x=".7" y=".7" width="12.6" height="9.6" fill="#03497f"/><path d="M1 1l6 5 6-5" fill="none" stroke="#fff" stroke-width="1.2"/></svg>
  <div class="abs flabel" style="left:338px;top:4055px">EMAIL</div>
  <div class="abs fline" style="left:338px;top:4073px">info@harborofmercy.org</div>
  <h4 class="abs" style="left:564px;top:3920px">Join Our Newsletter</h4>
  <div class="abs fline" style="left:564px;top:3950px;width:220px">Lorem Ipsum is simply text of the printing and typesetting.</div>
  <div class="abs" style="left:566px;top:4006px;width:237px;height:37px;border:1px solid #ccc;border-radius:2px;font-size:11.5px;color:#666;padding:11px 0 0 31px">Enter Your Email
    <svg class="abs" style="left:10px;top:12px" width="14" height="11" viewBox="0 0 14 11"><rect x=".7" y=".7" width="12.6" height="9.6" fill="none" stroke="#6a8bb0" stroke-width="1.2"/><path d="M1 1l6 5 6-5" fill="none" stroke="#6a8bb0" stroke-width="1.2"/></svg>
  </div>
  <a class="abs btn-blue" style="left:566px;top:4055px;width:237px;height:37px">Subscribe</a>
  <div class="abs brand" style="left:874px;top:3950px"><span class="sq"></span>Harbor of Mercy</div>
  <div class="abs round" style="left:914px;top:4026px;width:25px;height:25px"></div>
  <div class="abs" style="left:948px;top:4032px;font-size:12px;font-weight:600;color:var(--blue)">Follow Us</div>
</footer>
<div class="abs copy">© 2023 The Harbor of Mercy. All Rights Reserved.</div>

</body>
</html>
```